professional business card

A Clean looking business card for a money transfer company. Our company is call Velorix= Transfer + Send = Transcend (next level)
to show professionalism as well as some effects to show digital tech.

1 side to have position, name and address
2 side to have company name and show that we provide money exchange and cross-border money transfer

Target Market(s)

Remittance companies and high net worth individuals

Industry/Entity Type

Finance

Contact Information for Business Card

Name, address, email, title, services- money exchange and cross-border remittance

Requirements
Nice to have
• Digital age feel

```html
<!DOCTYPE html>
<html lang="en">
<head>
<meta charset="utf-8">
<title>Velorix business card</title>
<link href="https://fonts.googleapis.com/css2?family=Montserrat:wght@400;500;600&display=swap" rel="stylesheet">
<style>
  :root {
    --backdrop: #5e5d62;
    --card: #243240;
    --card-deep: #1d2934;
    --card-soft: #2c3b4a;
    --accent: #5ccfe0;
    --ink: #f2f5f7;
    --ink-muted: #d5dde3;
  }
  * { margin: 0; padding: 0; box-sizing: border-box; }
  html, body {
    width: 1200px; height: 876px; overflow: hidden;
    background: var(--backdrop);
    font-family: "Montserrat", sans-serif;
  }
  .canvas { position: relative; width: 1200px; height: 876px; }

  .card {
    position: absolute;
    width: 520px; height: 297px;
    background: var(--card);
    border-radius: 4px;
    overflow: hidden;
    box-shadow: 0 18px 30px rgba(0,0,0,.35);
  }

  /* Back side */
  .card--back { left: 610px; top: 110px; }
  .card--back .pattern-area {
    position: absolute; inset: 0;
    background: radial-gradient(ellipse at 50% 50%, var(--card-soft) 0%, var(--card) 55%, var(--card-deep) 100%);
  }
  .back-brand {
    position: absolute; inset: 0;
    display: flex; flex-direction: column; align-items: center; justify-content: center;
  }
  .wordmark {
    display: flex; align-items: center; gap: 12px;
    color: var(--ink); font-weight: 500; letter-spacing: 2px;
  }
  .wordmark__dot {
    width: 26px; height: 26px; border-radius: 50%; background: var(--accent);
  }
  .card--back .wordmark { font-size: 40px; }
  .card--back .wordmark__dot { width: 34px; height: 34px; }
  .tagline {
    margin-top: 14px; font-size: 12.5px; letter-spacing: 1.4px;
    color: var(--accent); font-weight: 500;
  }
  .tagline__joiner { color: var(--ink); }

  /* Front side */
  .card--front { left: 80px; top: 450px; }
  .card--front .map-area {
    position: absolute; left: 40px; top: 20px; width: 440px; height: 250px;
    background: radial-gradient(ellipse at 45% 50%, rgba(120,140,160,.22) 0%, rgba(120,140,160,.08) 55%, transparent 75%);
  }
  .front-brand { position: absolute; left: 40px; top: 128px; }
  .card--front .wordmark { font-size: 30px; }
  .divider {
    position: absolute; left: 268px; top: 70px; width: 2px; height: 150px;
    background: var(--ink-muted);
  }
  .divider::before {
    content: ""; position: absolute; left: 0; top: 30px; width: 2px; height: 90px;
    background: var(--accent);
  }
  .person { position: absolute; left: 292px; top: 70px; }
  .person__name {
    font-size: 19px; font-weight: 600; color: var(--accent); letter-spacing: 1px;
  }
  .person__title, .person__address {
    font-size: 12px; color: var(--ink-muted); line-height: 17px;
  }
  .person__title { margin: 3px 0 2px; }
  .contact { margin-top: 8px; list-style: none; }
  .contact__item {
    display: flex; align-items: center; gap: 8px;
    font-size: 12.5px; color: var(--ink); line-height: 20px; letter-spacing: .5px;
  }
  .contact__icon { width: 12px; height: 12px; flex: none; }
</style>
</head>
<body>
<main class="canvas">

  <section class="card card--back" aria-label="Card back">
    <div class="pattern-area" role="img" aria-label="Embossed repeating brand pattern"></div>
    <div class="back-brand">
      <div class="wordmark"><span class="wordmark__dot"></span>VELORIX</div>
      <p class="tagline">MONEY EXCHANGE <span class="tagline__joiner">AND</span> REMITTANCE</p>
    </div>
  </section>

  <section class="card card--front" aria-label="Card front">
    <div class="map-area" role="img" aria-label="Dotted world map"></div>
    <div class="front-brand">
      <div class="wordmark"><span class="wordmark__dot"></span>VELORIX</div>
    </div>
    <div class="divider"></div>
    <div class="person">
      <h1 class="person__name">LENA MARSH COLT</h1>
      <p class="person__title">Director</p>
      <p class="person__address">P.O. Box 7710<br>Harbor Falls, NY 40315</p>
      <ul class="contact">
        <li class="contact__item">
          <svg class="contact__icon" viewBox="0 0 12 12"><path d="M3 1 L5 3 L4 4.5 Q5 7 7.5 8 L9 7 L11 9 L9.5 11 Q4 10.5 1 2.5 Z" fill="#5ccfe0"/></svg>
          555-210-4477
        </li>
        <li class="contact__item">
          <svg class="contact__icon" viewBox="0 0 12 12"><rect x="1" y="2.5" width="10" height="7" fill="#5ccfe0"/><path d="M1 2.5 L6 7 L11 2.5" stroke="#243240" stroke-width="1" fill="none"/></svg>
          info@velorix.com
        </li>
        <li class="contact__item">
          <svg class="contact__icon" viewBox="0 0 12 12"><circle cx="6" cy="6" r="5" fill="none" stroke="#5ccfe0" stroke-width="1.2"/><ellipse cx="6" cy="6" rx="2.2" ry="5" fill="none" stroke="#5ccfe0" stroke-width="1"/><line x1="1" y1="6" x2="11" y2="6" stroke="#5ccfe0" stroke-width="1"/></svg>
          www.velorix.com
        </li>
      </ul>
    </div>
  </section>

</main>
</body>
</html>
```